Website redesign for Root and Renew

We would like to update the design of our current website to a more concise, conversion optimized design.
The goal of our website is to get our message across as concisely as possible plus encourage people to contact us for more information or to book a consultation.
We need a redesign of the home page and 1 internal page - just for design/layout purposes/format purposes.

Target Market(s)

Males 20-45 years old who are concerned about hair loss and who want to regrow their own hair.

Industry/Entity Type

Health And Wellness

Number of Pages Required

2 page

Font styles to use
Sans Serif

Colors
00a990
33a6d7
ffffff
9d9d9d

Requirements
Must have
• We want the home page to be very concise and to the point in getting the message across. We want to get across the following 6 key messages:
• 1. Dr Brambury story – why he created this solution
• 2. Hair loss is caused by a chemical imbalance
• 3. Root and renew conducts genetic and DNA analysis, then rebalances body chemistry, thus reversing the hair loss process and enabling your own hair to regrow naturally
• 4. Money back guaranteed results
• 5. Purely The Core ingredients – no harsh preservatives or chemicals are included
• 6. All ingredients are FDA approved and safe – no side effects
• We also need a strong call to action. We want people to call or email us to find out more information or to schedule a consultation.
• Here is our current website which is not performing as we would hope: http://www.rootandrenewhq.com/
• Here is our press release for further information: https://www.pressflarex.com/news/finally-we-now-have-a-cure-for-male-pattern-baldness-40528316
• I uploaded the logo files, but let me know if anything else is needed and I can add it.

```html
<!DOCTYPE html>
<html lang="en">
<head>
<meta charset="utf-8">
<title>Root &amp; Renew — Home</title>
<link rel="stylesheet" href="https://fonts.googleapis.com/css2?family=Raleway:wght@300;400;500;600;700&family=Open+Sans:ital,wght@0,400;0,600;0,700;1,400&display=swap">
<style>
:root{
  --teal:#00a990;
  --teal-dark:#0b7a69;
  --teal-deep:#0a4f45;
  --blue:#33a6d7;
  --grey:#9d9d9d;
  --grey-band:#8e8e8e;
  --mint:#e6f5f4;
  --ink:#333;
  --white:#fff;
}
*{box-sizing:border-box;margin:0;padding:0}
html,body{width:1200px;height:3782px;overflow:hidden}
body{font-family:"Open Sans",Arial,sans-serif;color:var(--ink);background:var(--white)}
.btn{display:inline-block;border:2px solid #777;color:#444;font:600 14px "Open Sans",sans-serif;padding:12px 24px;text-transform:uppercase;background:var(--white)}
.btn-teal{background:var(--teal);color:var(--white);border:3px solid #d9f2ee;font-size:22px;padding:9px 20px}
.section-title{font-family:"Raleway",sans-serif;font-weight:400;font-size:42px;text-align:center;color:var(--ink)}
.section-title .brand-caps{font-variant:small-caps;color:var(--teal)}
.divider{display:block;margin:12px auto 0;width:240px;height:20px}

/* top bar */
.topbar{height:50px;background:var(--teal-deep);display:flex;align-items:center}
.topbar-social{background:var(--teal);height:50px;width:420px;display:flex;gap:8px;align-items:center;padding-left:132px}
.topbar-social span{width:26px;height:26px;border-radius:50%;background:var(--white)}
.topbar-links{display:flex;align-items:center;gap:40px;color:var(--white);font-size:17px;margin-left:150px}
.topbar-call{margin-left:auto;background:var(--teal);height:50px;display:flex;align-items:center;gap:10px;padding:0 40px 0 30px;color:var(--white);font-size:15px}
.topbar-call b{font-size:21px}

/* nav */
.nav{height:90px;display:flex;align-items:center;padding:0 76px;border-bottom:1px solid #e5e5e5}
.brand{display:flex;align-items:center;gap:12px}
.brand-mark{width:40px;height:40px;background:var(--teal)}
.brand-name{font:500 30px "Raleway",sans-serif;color:var(--teal-dark);line-height:1}
.brand-by{font:400 15px "Raleway",sans-serif;color:var(--blue);margin-top:4px;padding-left:112px}
.nav-menu{margin-left:auto;display:flex;gap:30px;font-size:14px;color:var(--grey);text-transform:uppercase}
.nav-menu .active{color:var(--ink);font-weight:600}

/* hero */
.hero{height:536px;position:relative;background:linear-gradient(90deg,#eef5f6 0%,#e3eef0 50%,#d3e2e6 100%);overflow:hidden}
.hero-photo{position:absolute;right:0;top:0;width:500px;height:536px;background:linear-gradient(165deg,#d9e3e6 0%,#c79c7e 35%,#8f5f45 60%,#3b4f7a 82%,#2b3656 100%)}
.hero-copy{position:absolute;left:76px;top:44px;width:640px}
.hero-title{font:400 52px/1.1 "Raleway",sans-serif;color:var(--teal)}
.hero-title b{font-weight:700}
.hero-lead{font:700 21px/1.35 "Open Sans",sans-serif;color:#444;margin-top:20px}
.hero-sub{font-size:15px;line-height:1.5;color:#555;margin-top:12px;width:600px}
.hero .btn-teal{margin-top:18px}
.signup{position:absolute;left:76px;top:383px;width:980px;height:98px;display:flex;align-items:center}
.signup-text{height:98px;width:415px;background:rgba(51,166,215,.82);font:400 28px/1.2 "Raleway",sans-serif;color:var(--white);padding:18px 0 0 26px}
.signup-form{height:98px;flex:1;background:rgba(0,169,144,.9);display:flex;align-items:center;padding-left:24px}
.signup-input{width:360px;height:50px;border:1px solid rgba(255,255,255,.85);color:var(--white);font-size:14px;display:flex;align-items:center;padding-left:20px}
.signup-btn{height:50px;padding:0 28px;display:flex;align-items:center;background:var(--teal-dark);color:var(--white);font-size:22px;margin-left:8px}

/* why */
.why{height:597px;background:var(--mint);padding-top:60px}
.why-grid{display:flex;justify-content:space-between;width:1060px;margin:42px auto 0}
.why-item{width:240px;text-align:center}
.why-circle{width:226px;height:226px;border-radius:50%;border:7px solid var(--white);box-shadow:0 3px 8px rgba(0,0,0,.2);margin:0 auto}
.why-label{font:400 22px/1.15 "Raleway",sans-serif;color:#777;margin-top:22px;height:54px}
.why-label.hl{color:var(--teal)}
.why .btn{margin-top:24px}

/* story */
.story{height:466px;display:flex;padding:40px 79px 0 81px}
.story-copy{width:490px}
.story-title{font:400 40px "Raleway",sans-serif;color:#444}
.story-title .caps{font-variant:small-caps}
.story-kicker{font:600 19px "Open Sans",sans-serif;margin-top:14px}
.story-text{font-size:14.5px;line-height:1.72;color:#666;margin-top:8px}
.story .btn{margin-top:26px}
.story-video{margin-left:auto;width:500px;height:370px;position:relative;background:linear-gradient(120deg,#e8e4df 0%,#c99878 38%,#9a6d52 62%,#5a4436 100%)}
.video-bar{position:absolute;left:0;right:0;bottom:0;height:36px;background:rgba(0,0,0,.8)}

/* how */
.how{height:498px;background:linear-gradient(180deg,#3aa9d9 0%,#6cc0e4 45%,#3aa9d9 100%);padding-top:50px;text-align:center;color:var(--white)}
.how .section-title{color:var(--white)}
.how .section-title .brand-caps{color:var(--white)}
.how-steps{position:relative;width:820px;margin:36px auto 0;display:flex;justify-content:space-between}
.how-step{width:190px}
.how-circle{width:146px;height:146px;border-radius:50%;border:5px solid var(--white);margin:0 auto}
.how-label{font:500 19px "Raleway",sans-serif;margin-top:18px;text-transform:uppercase}
.how .btn-teal{margin-top:34px}

/* testimonials */
.testimonials{height:584px;padding-top:50px}
.t-grid{display:flex;justify-content:space-between;width:1040px;margin:36px auto 0}
.t-card{width:333px;background:#eef6fa}
.t-photo{height:212px;background:linear-gradient(180deg,#2f2520 0%,#4a3a30 22%,#b98b6d 45%,#d2a487 70%,#a8785c 100%);position:relative;border-bottom:2px solid var(--white)}
.t-photo::after{content:"";position:absolute;left:50%;top:0;bottom:0;width:2px;background:var(--white)}
.t-name{position:absolute;left:0;bottom:-6px;background:var(--teal);color:var(--white);font:600 17px "Open Sans",sans-serif;padding:6px 14px;z-index:1}
.t-quote{font:italic 400 14.5px/1.6 "Open Sans",sans-serif;color:#666;text-align:center;padding:24px 26px 28px}

/* blog */
.blog{height:610px;background:var(--grey-band);padding-top:50px}
.blog .section-title{color:var(--white)}
.b-grid{display:flex;justify-content:space-between;width:1040px;margin:34px auto 0}
.b-card{width:333px;background:var(--white);padding:10px 10px 26px;text-align:center}
.b-photo{height:208px}
.b-title{font:500 22px "Raleway",sans-serif;margin-top:18px;color:#333}
.b-text{font-size:14px;line-height:1.5;color:#666;margin-top:8px;padding:0 10px}
.b-card .btn{margin-top:18px}

/* footer */
.footer{height:286px;background:var(--blue);color:var(--white);display:flex;padding:44px 76px 0}
.f-col h4{font:400 24px "Raleway",sans-serif;margin-bottom:18px}
.f-col{font-size:14px;line-height:1.55}
.f-contact{width:265px}
.f-hours{width:265px}
.f-legal{width:250px}
.f-row{display:flex;gap:12px;margin-bottom:14px}
.f-row svg{flex:none;margin-top:3px}
.f-legal li{list-style:none;margin-bottom:6px}
.f-legal li::before{content:"›";margin-right:10px}
.f-brand{margin-left:auto;text-align:center;padding-top:40px}
.f-brand-name{font:500 26px "Raleway",sans-serif;color:var(--white)}
.f-social{display:flex;gap:8px;margin-top:30px}
.f-social span{width:30px;height:30px;border-radius:50%;border:2px solid var(--white)}
.f-social span:first-child{background:var(--teal-deep);border-color:var(--teal-deep)}
.copyright{height:65px;background:var(--teal-deep);color:#dfe;font-size:14px;display:flex;align-items:center;justify-content:center}
.copyright b{color:var(--teal);font-weight:600;margin:0 4px}
</style>
</head>
<body>

<header>
  <div class="topbar">
    <div class="topbar-social"><span></span><span></span><span></span><span></span><span></span><span></span></div>
    <div class="topbar-links"><span>EN</span><span>Talk To Us</span></div>
    <div class="topbar-call">
      <svg width="22" height="22" viewBox="0 0 24 24"><path fill="#fff" d="M6.6 10.8a15 15 0 006.6 6.6l2.2-2.2c.3-.3.7-.4 1-.2 1.1.4 2.3.6 3.6.6.6 0 1 .4 1 1V20c0 .6-.4 1-1 1A17 17 0 013 4c0-.6.4-1 1-1h3.5c.6 0 1 .4 1 1 0 1.3.2 2.5.6 3.6.1.3 0 .7-.2 1z"/></svg>
      Call Us On : <b>(310) 555-0142</b>
    </div>
  </div>
  <nav class="nav">
    <div>
      <div class="brand"><span class="brand-mark"></span><span class="brand-name">Root &amp; Renew</span></div>
      <div class="brand-by">by Elliot Brambury M.D.</div>
    </div>
    <div class="nav-menu">
      <span class="active">About</span><span>How it works</span><span>Success Stories</span><span>Partners</span><span>FAQs</span><span>Blog</span><span>Contact</span>
    </div>
  </nav>
</header>

<section class="hero">
  <div class="hero-photo" role="img" aria-label="Smiling young man with full dark hair in a blue plaid shirt"></div>
  <div class="hero-copy">
    <h1 class="hero-title">GET BACK THE ORIGINAL<br><b>DENSITY</b> OF YOUR HAIR</h1>
    <p class="hero-lead">The First Non-Surgical Hair Loss Solution With Clinically Proven Results 100% Money Back Guarantee! *</p>
    <p class="hero-sub">The Revolutionary New Solution For Hair Loss That Uses Personalized Medicine To Stop Hair Loss and Regrow Your Thinning / Receding Hair.</p>
    <span class="btn btn-teal">BOOK A CONSULTATION</span>
  </div>
  <div class="signup">
    <div class="signup-text">Receive Free Hair Regrowth Advice &amp; Special Offers</div>
    <div class="signup-form">
      <div class="signup-input">Enter Your Email</div>
      <div class="signup-btn">SUBSCRIBE</div>
    </div>
  </div>
</section>

<section class="why">
  <h2 class="section-title">Why <span class="brand-caps">Root &amp; reNew</span>?</h2>
  <svg class="divider" viewBox="0 0 240 20"><line x1="0" y1="6" x2="240" y2="6" stroke="#c9d9d7"/><circle cx="120" cy="10" r="8" fill="#9fc9c2"/></svg>
  <div class="why-grid">
    <div class="why-item"><div class="why-circle" role="img" aria-label="Young man with glasses running a hand through his hair" style="background:linear-gradient(160deg,#6fb3e6 0%,#2f7cc0 55%,#1f4f80 100%)"></div><div class="why-label">Root and Renew</div><span class="btn">Get Started</span></div>
    <div class="why-item"><div class="why-circle" role="img" aria-label="Hands holding banknotes" style="background:linear-gradient(160deg,#e6dccb 0%,#b9a98a 45%,#d5a98a 100%)"></div><div class="why-label hl">Money Back<br>Guaranteed Results</div><span class="btn">Know More</span></div>
    <div class="why-item"><div class="why-circle" role="img" aria-label="Doctor in green scrubs examining a patient's scalp" style="background:linear-gradient(160deg,#eef1ee 0%,#6cbfa6 50%,#3b6b5e 100%)"></div><div class="why-label">Purely The Core<br>Ingredients</div><span class="btn">Know More</span></div>
    <div class="why-item"><div class="why-circle" role="img" aria-label="Hands holding a card about side effects" style="background:linear-gradient(160deg,#f6efec 0%,#e5d2c8 55%,#c9504a 100%)"></div><div class="why-label">No Side Effects</div><span class="btn">FDA Approved</span></div>
  </div>
</section>

<section class="story">
  <div class="story-copy">
    <h2 class="story-title">Dr Brambury <span class="caps">Story</span></h2>
    <p class="story-kicker">why he created this solution</p>
    <p class="story-text">Dr. Elliot Brambury, the creator of Root and Renew is a renowned hair restoration expert. After seeing first his father and then older brothers thin and go bald, he dedicated his life to finding the cure for hair loss. After initially pioneering the single hair method for hair transplant, he determined there must be a non-surgical solution and spent the last 20 years in research and clinical trial and error first creating....</p>
    <span class="btn">Know More</span>
  </div>
  <div class="story-video" role="img" aria-label="Video still of a man checking his hairline in a mirror">
    <svg class="video-bar" viewBox="0 0 500 36" preserveAspectRatio="none">
      <rect x="14" y="11" width="4" height="14" fill="#fff"/><rect x="22" y="11" width="4" height="14" fill="#fff"/>
      <rect x="60" y="16" width="330" height="4" fill="#555"/><rect x="60" y="16" width="50" height="4" fill="#e22"/>
      <rect x="410" y="16" width="30" height="4" fill="#ccc"/>
      <rect x="470" y="10" width="16" height="16" fill="none" stroke="#fff" stroke-width="2"/>
    </svg>
  </div>
</section>

<section class="how">
  <h2 class="section-title">How <span class="brand-caps">Root &amp; reNew</span> Works?</h2>
  <svg class="divider" viewBox="0 0 240 20"><line x1="0" y1="6" x2="240" y2="6" stroke="#9fd3ea"/><circle cx="120" cy="10" r="8" fill="#d7eef8"/></svg>
  <div class="how-steps">
    <svg style="position:absolute;left:95px;top:6px" width="630" height="40" viewBox="0 0 630 40"><path d="M0 30 Q105 0 210 20 T420 20 T630 30" fill="none" stroke="#fff" stroke-width="2" stroke-dasharray="3 6"/></svg>
    <div class="how-step"><div class="how-circle" role="img" aria-label="Doctor consulting a patient" style="background:linear-gradient(160deg,#dfe8ee,#5f93c6)"></div><div class="how-label">Consultation</div></div>
    <div class="how-step"><div class="how-circle" role="img" aria-label="Portrait of a smiling bald man" style="background:linear-gradient(160deg,#e8e4de,#b08268)"></div><div class="how-label">Determine Cause</div></div>
    <div class="how-step"><div class="how-circle" role="img" aria-label="Specialist treating a patient's scalp" style="background:linear-gradient(160deg,#eef1ee,#4fae98)"></div><div class="how-label">Action Taken</div></div>
    <div class="how-step"><div class="how-circle" role="img" aria-label="Man running a hand through regrown hair" style="background:linear-gradient(160deg,#eae7e3,#9a6e55)"></div><div class="how-label">Regrow Hair</div></div>
  </div>
  <span class="btn btn-teal">BOOK A CONSULTATION</span>
</section>

<section class="testimonials">
  <h2 class="section-title">Testimonials</h2>
  <svg class="divider" viewBox="0 0 240 20"><line x1="0" y1="6" x2="240" y2="6" stroke="#ddd"/><circle cx="120" cy="10" r="8" fill="#9fc9c2"/></svg>
  <div class="t-grid">
    <div class="t-card"><div class="t-photo" role="img" aria-label="Before and after photos of a client's hairline"><span class="t-name">Marcus Hale</span></div><p class="t-quote">" Lorem Ipsum is simply dummy text of the printing and typesetting industry. Lorem Ipsum has been the industry's standard dummy text ever since the 1500s. "</p></div>
    <div class="t-card"><div class="t-photo" role="img" aria-label="Before and after photos of a client's hairline"><span class="t-name">Owen Tarrant</span></div><p class="t-quote">" Lorem Ipsum is simply dummy text of the printing and typesetting industry. Lorem Ipsum has been the industry's standard dummy text ever since the 1500s. "</p></div>
    <div class="t-card"><div class="t-photo" role="img" aria-label="Before and after photos of a client's hairline"><span class="t-name">Owen Tarrant</span></div><p class="t-quote">" Lorem Ipsum is simply dummy text of the printing and typesetting industry. Lorem Ipsum has been the industry's standard dummy text ever since the 1500s. "</p></div>
  </div>
</section>

<section class="blog">
  <h2 class="section-title">Latest From Blog</h2>
  <svg class="divider" viewBox="0 0 240 20"><line x1="0" y1="6" x2="240" y2="6" stroke="#b5b5b5"/><circle cx="120" cy="10" r="8" fill="#ccc"/></svg>
  <div class="b-grid">
    <div class="b-card"><div class="b-photo" role="img" aria-label="Man examining his hairline" style="background:linear-gradient(120deg,#f1ede8 0%,#d2a587 45%,#8e5e43 100%)"></div><h3 class="b-title">Lorem Ipsum is simply</h3><p class="b-text">Book an obligation free market appraisal with one of our area specialists.</p><span class="btn">Know More</span></div>
    <div class="b-card"><div class="b-photo" role="img" aria-label="Man with short hair looking concerned" style="background:linear-gradient(120deg,#f5f4f2 0%,#c9b2a2 50%,#7d6657 100%)"></div><h3 class="b-title">Lorem Ipsum is simply</h3><p class="b-text">Book an obligation free market appraisal with one of our area specialists.</p><span class="btn">Know More</span></div>
    <div class="b-card"><div class="b-photo" role="img" aria-label="Man relaxing on grass with his dog" style="background:linear-gradient(120deg,#a5cf5c 0%,#6f9b3a 45%,#3c3a34 100%)"></div><h3 class="b-title">Lorem Ipsum is simply</h3><p class="b-text">Book an obligation free market appraisal with one of our area specialists.</p><span class="btn">Know More</span></div>
  </div>
</section>

<footer>
  <div class="footer">
    <div class="f-col f-contact">
      <h4>Contact Information</h4>
      <div class="f-row"><svg width="16" height="20" viewBox="0 0 16 20"><path fill="#fff" d="M8 0a8 8 0 00-8 8c0 6 8 12 8 12s8-6 8-12a8 8 0 00-8-8zm0 11a3 3 0 110-6 3 3 0 010 6z"/></svg><div><b>ROOT &amp; RENEW</b><br>2810 Larkspur Ave, Suite 210<br>Fairview CA 90418</div></div>
      <div class="f-row"><svg width="16" height="16" viewBox="0 0 24 24"><path fill="#fff" d="M6.6 10.8a15 15 0 006.6 6.6l2.2-2.2c.3-.3.7-.4 1-.2 1.1.4 2.3.6 3.6.6.6 0 1 .4 1 1V20c0 .6-.4 1-1 1A17 17 0 013 4c0-.6.4-1 1-1h3.5c.6 0 1 .4 1 1 0 1.3.2 2.5.6 3.6.1.3 0 .7-.2 1z"/></svg><div>(310) 555-0142</div></div>
      <div class="f-row"><svg width="16" height="12" viewBox="0 0 16 12"><rect width="16" height="12" fill="#fff"/><path d="M0 0l8 6 8-6" fill="none" stroke="#33a6d7" stroke-width="1.5"/></svg><div>info@rootandrenewhq.com</div></div>
    </div>
    <div class="f-col f-hours">
      <h4>Hours of Operation</h4>
      <div class="f-row"><svg width="14" height="14" viewBox="0 0 14 14"><circle cx="7" cy="7" r="6" fill="none" stroke="#fff" stroke-width="1.5"/><path d="M7 3.5V7h2.5" fill="none" stroke="#fff" stroke-width="1.5"/></svg><div>Monday -<br><b>Friday: 9.00am to 5.00pm</b></div></div>
      <div class="f-row"><svg width="14" height="14" viewBox="0 0 14 14"><circle cx="7" cy="7" r="6" fill="none" stroke="#fff" stroke-width="1.5"/><path d="M7 3.5V7h2.5" fill="none" stroke="#fff" stroke-width="1.5"/></svg><div>Saturday -<br><b>8.00am to 2.00pm</b></div></div>
    </div>
    <div class="f-col f-legal">
      <h4>Legal Info</h4>
      <ul><li>Home</li><li>Contact</li><li>Privacy Policy</li><li>Terms &amp; Conditions</li></ul>
    </div>
    <div class="f-brand">
      <div class="f-brand-name">Root &amp; Renew</div>
      <div class="f-social"><span></span><span></span><span></span><span></span><span></span><span></span></div>
    </div>
  </div>
  <div class="copyright">© <b>ROOT &amp; RENEW</b> - 2017. All Rights Reserved</div>
</footer>

</body>
</html>
```